Business Card Design Project

Financial planning, Insurance and Real estate - Financial Services company

Contact Information for Business Card

Looking for something simple in design -
Tolverin Equity LLC
Tolverin Wealth Managment

```html
<!DOCTYPE html>
<html lang="en">
<head>
<meta charset="utf-8">
<title>Tolverin Wealth Management – Business Card</title>
<link rel="stylesheet" href="https://fonts.googleapis.com/css2?family=Open+Sans:wght@400;600&family=PT+Sans+Narrow:wght@700&display=swap">
<style>
  :root {
    --stage: #3b3c3e;
    --card-white: #e4e4e5;
    --brand-blue: #0a7fc0;
    --ink: #3a3a3a;
    --rule: #9a9a9a;
    --white: #ffffff;
  }
  * { box-sizing: border-box; margin: 0; padding: 0; }
  html, body {
    width: 1200px; height: 896px; overflow: hidden;
    background: var(--stage);
    font-family: "Open Sans", Arial, sans-serif;
  }
  .sheet {
    width: 1200px; height: 896px;
    display: flex; align-items: center; justify-content: center; gap: 50px;
  }
  .card {
    width: 540px; height: 309px;
    position: relative; overflow: hidden;
    box-shadow: 0 10px 24px rgba(0,0,0,.45);
  }
  /* Front */
  .card--front { background: var(--card-white); color: var(--ink); }
  .contact { position: absolute; left: 42px; top: 44px; width: 250px; }
  .contact__name {
    font-family: "PT Sans Narrow", Arial, sans-serif; font-weight: 700;
    font-size: 27px; color: var(--brand-blue); line-height: 1;
  }
  .contact__title { font-size: 15px; margin-top: 2px; }
  .contact__rule { height: 1px; background: var(--rule); margin: 10px 0 8px; width: 230px; }
  .contact__list { list-style: none; font-size: 15px; line-height: 21px; }
  .contact__list li { display: flex; align-items: center; gap: 8px; }
  .contact__list svg { width: 13px; height: 13px; fill: var(--brand-blue); flex: none; }

  .company { position: absolute; right: 40px; top: 150px; width: 270px; text-align: right; }
  .company__name {
    display: inline-flex; align-items: center; gap: 8px;
    font-family: "PT Sans Narrow", Arial, sans-serif; font-weight: 700;
    font-size: 20px; color: var(--brand-blue);
  }
  .company__dot { width: 14px; height: 14px; border-radius: 50%; background: var(--brand-blue); }
  .company__rule { height: 1px; background: var(--rule); margin: 14px 0 10px; }
  .services { list-style: none; font-size: 16px; line-height: 21px; }
  .services li::after {
    content: ""; display: inline-block; width: 6px; height: 6px; border-radius: 50%;
    background: var(--brand-blue); margin-left: 8px; vertical-align: middle;
  }
  .services li:nth-child(2) { margin-right: 10px; }
  .services li:nth-child(3) { margin-right: 20px; }

  /* Back */
  .card--back { background: var(--brand-blue); color: var(--white); }
  .back__brand {
    position: absolute; left: 0; right: 0; top: 118px;
    display: flex; align-items: center; justify-content: center; gap: 12px;
    font-family: "PT Sans Narrow", Arial, sans-serif; font-weight: 700; font-size: 30px;
  }
  .back__dot { width: 22px; height: 22px; border-radius: 50%; background: var(--white); }
  .back__web {
    position: absolute; left: 0; right: 0; bottom: 56px; text-align: center;
    font-size: 16px; letter-spacing: .5px;
  }
</style>
</head>
<body>
<main class="sheet">
  <section class="card card--front" aria-label="Business card front">
    <div class="contact">
      <h1 class="contact__name">Daniel Harwick</h1>
      <p class="contact__title">Managing Director</p>
      <div class="contact__rule"></div>
      <ul class="contact__list">
        <li><svg viewBox="0 0 16 16" aria-hidden="true"><path d="M3 1l3 3-2 2c1 2 4 5 6 6l2-2 3 3-2 2C7 15 1 9 1 3z"/></svg>044-555 010 270</li>
        <li><svg viewBox="0 0 16 16" aria-hidden="true"><path d="M4 0h8v16H4zM5.5 2v10h5V2zM7 13.5h2v1H7z" fill-rule="evenodd"/></svg>044-555 010 270</li>
        <li><svg viewBox="0 0 16 16" aria-hidden="true"><path d="M0 3h16v10H0zM1 4l7 5 7-5v-.5H1z"/></svg>info@tolverin.com</li>
      </ul>
    </div>
    <div class="company">
      <div class="company__name"><span class="company__dot"></span>Tolverin Wealth Management</div>
      <div class="company__rule"></div>
      <ul class="services">
        <li>Financial Planning</li>
        <li>Insurance</li>
        <li>Real Estate</li>
      </ul>
    </div>
  </section>

  <section class="card card--back" aria-label="Business card back">
    <div class="back__brand"><span class="back__dot"></span>Tolverin</div>
    <p class="back__web">www.tolverinwealth.com</p>
  </section>
</main>
</body>
</html>
```